Redesign two student school awards

I need to redesign 2 students awards. I need the elements of the letterhead to be incorporated into the Student Awards. I have covered some of the letterhead elements to show just the 4 elements that need to be incorporated: school emblem, school name, "For so much, what shall we repay?", and the 3 coloured ribbon. The awards need to be in colour and the use of the 3 school colours - purple, yellow (gold) and chocolate brown,

I have upload the 2 awards the school presents to students (they are printed on A4 Paper). The first one is the:

(1) Year Adviser Award - this award needs to include the school name; the title: Year Adviser's Award; Award to; Name (where the word is deleted and the office staff type the students name or uploaded names which can be autofilled); for the following achievements; the year (which can be changed an include the day and month (but auto filled); Year Adviser (where the teacher signs their name - see lower left of the award; (also the 5 categories - School Service, Community Service , Sporting Achievements, Leadership, Academic Achievement (these 5 categories must be able to be deleted as a student may receive the Year Adviser's Award for 1 or 2 of the categories)

(2) Principal's Award - all elements of this award need to be included. In this example there's a fake name Luke Dawson - this is where the office staff type in the students name or hopefully upload a list of names that are auto filled. The 5 categories need to be retained e.g. School Service, Community Service etc (these can be fixed as they are not deleted; for the following achievements; the year (which can be changed an include the day and month (but auto filled); my name and title,

For the 2 student awards it would be good if the design is in a computer program where the office staff can auto fill students names.

The main goal is to redesign the 2 awards, whilst retaining current elements and include 4 of the elements from the letter head.

Target Market(s)

School students (12 years old to 18 years old)

Industry/Entity Type

Education

Font styles to use
Serif

Requirements
Must have
• The elements and school colours mentioned in the description. Would be helpful if the computer program it is contained in allows for auto fill of student names, date, and for the Year Advisers award any one of the five award categories can be removed. To be printed on A4 paper/card

Colours must contain the school colours as mentioned before and the 4 elements of the letterhead. I am trying to have all our communications and awards contain similar elements.

```html
<!DOCTYPE html>
<html lang="en">
<head>
<meta charset="utf-8">
<title>Ridgeway Memorial High School – Student Awards</title>
<link rel="stylesheet" href="https://fonts.googleapis.com/css2?family=Noto+Serif:ital,wght@1,700&family=Libre+Baskerville:wght@700&family=Roboto:ital,wght@0,400;0,700;1,400&display=swap">
<style>
  :root {
    --stage: #b02aa4;
    --paper: #f5f5f6;
    --purple: #933489;
    --gold: #ece513;
    --chocolate: #2c0d13;
    --ink: #111111;
    --white: #ffffff;
  }
  * { box-sizing: border-box; margin: 0; padding: 0; }
  html, body { width: 1200px; height: 1101px; overflow: hidden; }
  body { background: var(--stage); position: relative; font-family: "Roboto", sans-serif; }

  .award {
    position: absolute;
    top: 207px;
    width: 458px;
    height: 657px;
    background: var(--paper);
    overflow: hidden;
    color: var(--ink);
    text-align: center;
    --accent: var(--chocolate);
  }
  .award--principal { left: 130px; }
  .award--adviser { left: 617px; --accent: var(--purple); }

  .award__art { position: absolute; inset: 0; width: 100%; height: 100%; }

  .award__motto {
    position: absolute; top: 72px; left: 0; right: 0;
    font: italic 400 12px "Roboto", sans-serif;
  }
  .award__school {
    position: absolute; top: 88px; left: 0; right: 0;
    font: italic 700 17px "Noto Serif", serif;
    letter-spacing: 0.4px;
    white-space: nowrap;
  }
  .award__title {
    position: absolute; top: 111px; left: 0; right: 0;
    font: 400 14px "Roboto", sans-serif;
    letter-spacing: 0.6px;
  }
  .award__emblem {
    position: absolute; top: 205px; left: 0; right: 0;
    display: flex; align-items: center; justify-content: center; gap: 8px;
    font: 700 28px "Libre Baskerville", serif;
    color: var(--chocolate);
  }
  .award__emblem-dot {
    width: 16px; height: 16px; border-radius: 50%; background: var(--purple);
  }
  .award__awarded {
    position: absolute; top: 308px; left: 0; right: 0;
    display: flex; align-items: center; justify-content: center; gap: 8px;
    font: 400 21px "Roboto", sans-serif;
  }
  .award__arrow { width: 114px; height: 14px; }
  .award__recipient {
    position: absolute; top: 342px; left: 0; right: 0;
    font: italic 700 40px/52px "Noto Serif", serif;
    letter-spacing: 1px;
    white-space: nowrap;
  }
  .award__for {
    position: absolute; top: 404px; left: 0; right: 0;
    font: italic 400 14px "Roboto", sans-serif;
    letter-spacing: 1px;
  }
  .award__categories {
    position: absolute; top: 436px; left: 0; right: 0;
    list-style: none;
    font: italic 700 17px/24px "Noto Serif", serif;
    letter-spacing: 1px;
    color: var(--white);
  }
  .award__signatory {
    position: absolute; left: 24px; top: 594px; text-align: left;
  }
  .award__signatory-role { font: italic 400 13px "Roboto", sans-serif; letter-spacing: 0.5px; color: var(--chocolate); }
  .award__signatory-name { font: 700 16px "Libre Baskerville", serif; }
  .award__year {
    position: absolute; left: 382px; top: 613px;
    width: 48px; height: 17px;
    background: var(--gold);
    font: 700 13px/17px "Roboto", sans-serif;
    letter-spacing: 1px;
  }
</style>
</head>
<body>

<section class="award award--principal">
  <svg class="award__art" viewBox="0 0 458 657" aria-hidden="true">
    <defs>
      <linearGradient id="ribbon-principal" x1="0" y1="0" x2="1" y2="0.3">
        <stop offset="0" stop-color="#933489"/>
        <stop offset="0.5" stop-color="#2c0d13"/>
        <stop offset="1" stop-color="#ece513"/>
      </linearGradient>
    </defs>
    <rect role="img" aria-label="Three-colour school ribbon in purple, chocolate and gold" x="0" y="16" width="458" height="50" fill="url(#ribbon-principal)"/>
    <rect role="img" aria-label="Flame ornament, left" x="18" y="364" width="46" height="33" rx="6" fill="var(--accent)"/>
    <rect role="img" aria-label="Flame ornament, right" x="394" y="364" width="46" height="33" rx="6" fill="var(--accent)"/>
    <rect x="0" y="397" width="458" height="6" fill="var(--accent)"/>
    <rect x="0" y="403" width="458" height="19" fill="var(--gold)"/>
    <path d="M0 430 L0 422 L458 422 L458 430 C440 470 452 560 330 584 C280 592 250 590 229 612 C208 590 178 592 128 584 C6 560 18 470 0 430 Z" fill="var(--accent)" stroke="var(--gold)" stroke-width="12" paint-order="stroke"/>
  </svg>

  <p class="award__motto">For so much, what shall we repay?</p>
  <h1 class="award__school">RIDGEWAY MEMORIAL HIGH SCHOOL</h1>
  <p class="award__title">Principal’s Award</p>
  <div class="award__emblem"><span class="award__emblem-dot"></span>Ridgeway</div>

  <p class="award__awarded">
    <svg class="award__arrow" viewBox="0 0 114 14" aria-hidden="true"><path d="M2 7 H112 M2 7 l7 -6 M2 7 l7 6 M8 7 l7 -6 M8 7 l7 6" stroke="var(--ink)" stroke-width="1.4" fill="none"/></svg>
    Awarded to
    <svg class="award__arrow" viewBox="0 0 114 14" aria-hidden="true"><path d="M2 7 H112 M112 7 l-7 -6 M112 7 l-7 6 M106 7 l-7 -6 M106 7 l-7 6" stroke="var(--ink)" stroke-width="1.4" fill="none"/></svg>
  </p>
  <p class="award__recipient">Luke Dawson</p>
  <p class="award__for">for the following achievements</p>
  <ul class="award__categories">
    <li>School Service</li>
    <li>Community Service</li>
    <li>Sporting Achievement</li>
    <li>Leadership</li>
    <li>Academic Achievement</li>
  </ul>
  <div class="award__signatory">
    <p class="award__signatory-role">Principal:</p>
    <p class="award__signatory-name">Mr P. Holloway</p>
  </div>
  <p class="award__year">2020</p>
</section>

<section class="award award--adviser">
  <svg class="award__art" viewBox="0 0 458 657" aria-hidden="true">
    <defs>
      <linearGradient id="ribbon-adviser" x1="0" y1="0" x2="1" y2="0.3">
        <stop offset="0" stop-color="#933489"/>
        <stop offset="0.5" stop-color="#2c0d13"/>
        <stop offset="1" stop-color="#ece513"/>
      </linearGradient>
    </defs>
    <rect role="img" aria-label="Three-colour school ribbon in purple, chocolate and gold" x="0" y="16" width="458" height="50" fill="url(#ribbon-adviser)"/>
    <rect role="img" aria-label="Flame ornament, left" x="18" y="364" width="46" height="33" rx="6" fill="var(--accent)"/>
    <rect role="img" aria-label="Flame ornament, right" x="394" y="364" width="46" height="33" rx="6" fill="var(--accent)"/>
    <rect x="0" y="397" width="458" height="6" fill="var(--accent)"/>
    <rect x="0" y="403" width="458" height="19" fill="var(--gold)"/>
    <path d="M0 430 L0 422 L458 422 L458 430 C440 470 452 560 330 584 C280 592 250 590 229 612 C208 590 178 592 128 584 C6 560 18 470 0 430 Z" fill="var(--accent)" stroke="var(--gold)" stroke-width="12" paint-order="stroke"/>
  </svg>

  <p class="award__motto">For so much, what shall we repay?</p>
  <h1 class="award__school">RIDGEWAY MEMORIAL HIGH SCHOOL</h1>
  <p class="award__title">Year Adviser’s Award</p>
  <div class="award__emblem"><span class="award__emblem-dot"></span>Ridgeway</div>

  <p class="award__awarded">
    <svg class="award__arrow" viewBox="0 0 114 14" aria-hidden="true"><path d="M2 7 H112 M2 7 l7 -6 M2 7 l7 6 M8 7 l7 -6 M8 7 l7 6" stroke="var(--ink)" stroke-width="1.4" fill="none"/></svg>
    Awarded to
    <svg class="award__arrow" viewBox="0 0 114 14" aria-hidden="true"><path d="M2 7 H112 M112 7 l-7 -6 M112 7 l-7 6 M106 7 l-7 -6 M106 7 l-7 6" stroke="var(--ink)" stroke-width="1.4" fill="none"/></svg>
  </p>
  <p class="award__recipient">Luke Dawson</p>
  <p class="award__for">for the following achievements</p>
  <ul class="award__categories">
    <li>School Service</li>
    <li>Community Service</li>
    <li>Sporting Achievement</li>
    <li>Leadership</li>
    <li>Academic Achievement</li>
  </ul>
  <div class="award__signatory">
    <p class="award__signatory-role">Principal:</p>
    <p class="award__signatory-name">Mr P. Holloway</p>
  </div>
  <p class="award__year">2020</p>
</section>

</body>
</html>
```